Web Site Design

Good Day.
We would like to design a new web site.
We currently have an existing web site but it is old and not in line with modern day websites, therefore we would like to create a new web site.
our current website = www.travenqo.com.au
Currently when someone does a search on zendrix for the word "Morvath" we appear as no 1. Therefore with the new website, we need to ensure that we maintain the number 1 rating in zendrix.
It is our preference that our new website looks similar to one of the below: (We are able to supply technology based pictures)
- www.halvor.com
- www.quellmarkgroup.com
- www.tollerbyit.com.au
- www.vexiron.com.au/
- www.grendaleit.com.au
- www.kroa.com/au/en/
A mixture of tollerbyit, Halvor and KROA/Vexiron are our favourite.
We like the appearance of KROA and Vexiron, where the picture stretches from one end of the page right across to the other end.
We would like to include a news ticker where we can advertise recent morvath new stories. As seen on the front page of Halvor or KROA. And we like some of the layout of tollerbyit where on the front page they have some icons below the main front page picture and also the associated vendors that they work with
It is our preference that the content from the old website be used to create the new website. Although we will add some additional content to the new website

```html
<!DOCTYPE html>
<html lang="en">
<head>
<meta charset="utf-8">
<title>Morvath — Advanced IP Communications</title>
<link rel="stylesheet" href="https://fonts.googleapis.com/css2?family=Open+Sans:wght@300;400;600;700&display=swap">
<style>
  :root {
    --orange: #f0890f;
    --orange-dark: #d86f00;
    --text-dark: #333333;
    --text-mid: #555555;
    --text-light: #888888;
    --line: #d6d6d6;
    --header-top: #ffffff;
    --header-bottom: #e6e6e6;
    --hero-bg: #efefef;
    --page-bg: #ffffff;
    --footer-bg: #f7f7f7;
  }
  * { box-sizing: border-box; margin: 0; padding: 0; }
  html, body { width: 1200px; height: 1101px; overflow: hidden; }
  body { position: relative; background: var(--page-bg); font-family: "Open Sans", Arial, sans-serif; color: var(--text-mid); }

  .site-header { position: absolute; left: 0; top: 0; width: 1200px; height: 106px;
    background: linear-gradient(var(--header-top), var(--header-bottom)); border-bottom: 1px solid #dcdcdc; }
  .brand { position: absolute; left: 109px; top: 36px; }
  .brand-name { font-size: 30px; font-weight: 700; color: #6b6b6b; letter-spacing: 1px; line-height: 1; }
  .brand-tagline { font-size: 9.5px; color: #555; margin-top: 2px; }
  .main-nav { position: absolute; left: 356px; top: 52px; display: flex; }
  .main-nav a { font-size: 16px; color: #555; text-decoration: none; padding: 0 16px; border-left: 1px solid #c8c8c8; line-height: 20px; }
  .main-nav a:first-child { border-left: none; }
  .search { position: absolute; left: 892px; top: 48px; width: 211px; height: 27px; border: 1px solid #c6c6c6; border-radius: 14px; background: #fff; }
  .search span { position: absolute; left: 13px; top: 6px; font-size: 11px; font-style: italic; color: #777; }
  .search svg { position: absolute; right: 9px; top: 6px; }

  .hero { position: absolute; left: 0; top: 107px; width: 1200px; height: 420px;
    background: radial-gradient(ellipse at 70% 40%, #ffffff 0%, #f6f6f6 45%, var(--hero-bg) 100%); }
  .hero-kicker { position: absolute; left: 106px; top: 102px; font-size: 28px; font-weight: 400; color: #555; }
  .hero-title { position: absolute; left: 106px; top: 137px; font-size: 38px; font-weight: 700; color: var(--orange); }
  .hero-text { position: absolute; left: 109px; top: 190px; width: 440px; font-size: 13px; line-height: 23px; color: #777; }
  .btn { position: absolute; left: 109px; top: 245px; width: 122px; height: 36px; border-radius: 3px;
    background: linear-gradient(#f79a22, var(--orange-dark)); color: #fff; font-size: 13px; text-align: center; line-height: 36px; }
  .dots { position: absolute; left: 107px; top: 312px; display: flex; gap: 6px; }
  .dots i { width: 15px; height: 15px; border-radius: 50%; border: 1px solid #bbb; background: #fff; }
  .dots i.active { background: var(--orange); border-color: var(--orange); }
  .hero-visual { position: absolute; left: 665px; top: 20px; width: 440px; height: 350px;
    background: radial-gradient(ellipse at 50% 60%, #dadada 0%, #eeeeee 60%, rgba(240,240,240,0) 100%); }

  .news-bar { position: absolute; left: 0; top: 527px; width: 1200px; height: 37px; background: var(--orange); color: #fff; }
  .news-label { position: absolute; left: 105px; top: 9px; font-size: 14px; font-weight: 600; }
  .news-arrow { position: absolute; top: 0; width: 36px; height: 37px; border-left: 1px solid rgba(255,255,255,.5); }
  .news-arrow svg { position: absolute; left: 12px; top: 11px; }
  .news-text { position: absolute; left: 287px; top: 10px; font-size: 12.5px; }

  .features { position: absolute; left: 95px; top: 589px; width: 1010px; height: 141px; border: 1px solid var(--line);
    display: flex; background: linear-gradient(#fff 60%, #f1f1f1); }
  .feature { flex: 1; position: relative; border-left: 1px solid var(--line); }
  .feature:first-child { border-left: none; }
  .feature-photo { position: absolute; left: 13px; top: 17px; width: 111px; height: 105px; }
  .feature h3 { position: absolute; left: 134px; top: 20px; font-size: 20px; font-weight: 400; color: var(--text-dark); white-space: nowrap; }
  .feature p { position: absolute; left: 137px; top: 50px; width: 190px; font-size: 12px; line-height: 20px; color: var(--text-light); }

  .welcome { position: absolute; left: 97px; top: 770px; width: 420px; }
  .welcome h2 { font-size: 26px; font-weight: 300; color: var(--text-dark); }
  .welcome .lead { margin-top: 10px; font-size: 14px; line-height: 22px; color: var(--text-mid); }
  .welcome .body { margin-top: 8px; font-size: 11.5px; line-height: 22px; color: var(--text-light); }

  .column { position: absolute; top: 770px; width: 265px; }
  .column h2 { font-size: 22px; font-weight: 400; color: var(--orange); }
  .column-photo { margin-top: 6px; width: 246px; height: 96px; border: 1px solid #ccc; }
  .column p { margin-top: 8px; font-size: 11.5px; line-height: 20px; color: var(--text-light); }

  .site-footer { position: absolute; left: 0; top: 1027px; width: 1200px; height: 74px; border-top: 1px solid #ddd; background: var(--footer-bg); }
  .copyright { position: absolute; left: 107px; top: 30px; font-size: 12px; color: #444; }
  .footer-nav { position: absolute; left: 574px; top: 30px; display: flex; gap: 27px; }
  .footer-nav a { font-size: 13px; color: #444; text-decoration: none; }
  .social { position: absolute; left: 1007px; top: 24px; display: flex; gap: 9px; }
  .social i { width: 22px; height: 22px; border-radius: 2px; background: #5b7fb5; }
</style>
</head>
<body>
  <header class="site-header">
    <div class="brand">
      <div class="brand-name">MORVATH</div>
      <div class="brand-tagline">Advanced IP Communications</div>
    </div>
    <nav class="main-nav">
      <a href="#">HOME</a><a href="#">SOLUTIONS</a><a href="#">SERVICES</a><a href="#">COMPANY</a><a href="#">CONTACT</a>
    </nav>
    <div class="search">
      <span>Search here..</span>
      <svg width="15" height="15" viewBox="0 0 15 15"><circle cx="6" cy="6" r="4.5" fill="none" stroke="#777" stroke-width="2"/><line x1="9.5" y1="9.5" x2="13.5" y2="13.5" stroke="#777" stroke-width="2.5" stroke-linecap="round"/></svg>
    </div>
  </header>

  <section class="hero">
    <div class="hero-kicker">Delivering Business Value through</div>
    <h1 class="hero-title">Advanced IP Communications</h1>
    <p class="hero-text">Etiam eu urna Sed porta Suspendisse quam leo molestie sed luctus quis feugiat in pede Fusce tellus Sed metus augue,</p>
    <div class="btn">READ MORE</div>
    <div class="dots"><i class="active"></i><i></i><i></i><i></i></div>
    <div class="hero-visual" role="img" aria-label="Illustration of a hand sketching business charts and a city skyline rising from an open book"></div>
  </section>

  <section class="news-bar">
    <div class="news-label">Latest News</div>
    <div class="news-arrow" style="left:203px"><svg width="12" height="16" viewBox="0 0 12 16"><polyline points="9,1 2,8 9,15" fill="none" stroke="#fff" stroke-width="1.5"/></svg></div>
    <div class="news-arrow" style="left:239px;border-right:1px solid rgba(255,255,255,.5)"><svg width="12" height="16" viewBox="0 0 12 16"><polyline points="3,1 10,8 3,15" fill="none" stroke="#fff" stroke-width="1.5"/></svg></div>
    <div class="news-text">Duis tincidunt lectus qui: dui viverra vestibulum Suspendisse vulputate aliquam</div>
  </section>

  <section class="features">
    <article class="feature">
      <div class="feature-photo" role="img" aria-label="Photo of a businessman touching a glowing digital interface" style="background:linear-gradient(135deg,#1c3050,#3d6a9a 55%,#17263f)"></div>
      <h3>Technical Specialist</h3>
      <p>Etiam eu urna Sed porta Suspendisse quam leo molestie sed luctus quis feugiat</p>
    </article>
    <article class="feature">
      <div class="feature-photo" role="img" aria-label="Photo of a smiling business team" style="background:linear-gradient(135deg,#d9c2ad,#8fa6c2 60%,#e6e6e6)"></div>
      <h3>Services Provide</h3>
      <p>Etiam eu urna Sed porta Suspendisse quam leo molestie sed luctus quis feugiat</p>
    </article>
    <article class="feature">
      <div class="feature-photo" role="img" aria-label="Photo of a presenter at a flip chart in a meeting" style="background:linear-gradient(135deg,#e9e5dc,#9b6b3c 60%,#3c2a1c)"></div>
      <h3>Why Choose Us</h3>
      <p>Etiam eu urna Sed porta Suspendisse quam leo molestie sed luctus quis feugiat</p>
    </article>
  </section>

  <section class="welcome">
    <h2>Welcome to Our Website Mainpage</h2>
    <p class="lead">Duis tincidunt lectus quis dui viverra vestibulum. Suspendisse vulputate aliquam dui Nulla elementum dui</p>
    <p class="body">Aliquam vehicula mi at mauris. Maecenas placerat, nisl at consequat rhoncus, sem nunc gravida justo, quis eleifend arcu velit quis lacus. Morbi magna magna, tincidunt a, mattis non, imperdiet vitae, tellus. Sed odio est, auctor ac, sollicitudin in, consequat vitae, orci. Fusce id felis. Vivamus sollicitudin metus eget eros.</p>
  </section>

  <section class="column" style="left:554px">
    <h2>About Morvath</h2>
    <div class="column-photo" role="img" aria-label="Photo of colleagues shaking hands across a meeting table" style="background:linear-gradient(135deg,#e4ecf5,#8aa7c9 55%,#dfe6ee)"></div>
    <p>Aliquam vehicula mi at mauris. Maecenas placerat, nisl at consequat rhoncus, sem nunc gravida justo, quis eleifend arcu velit</p>
  </section>

  <section class="column" style="left:837px">
    <h2>Recent Blog Post</h2>
    <div class="column-photo" role="img" aria-label="Photo of hands reviewing charts on a tablet" style="background:linear-gradient(135deg,#c9b39e,#f2f2f2 50%,#5b86c2)"></div>
    <p>Morbi diam mauris, viverra in, gravida eu, mattis in, ante. Morbi eget arcu. Morbi porta, libero id ullamcorper</p>
  </section>

  <footer class="site-footer">
    <div class="copyright">© 2013 Company Name.&nbsp; All right reserved.&nbsp; Term of Use</div>
    <nav class="footer-nav">
      <a href="#">HOME</a><a href="#">SOLUTIONS</a><a href="#">SERVICES</a><a href="#">COMPANY</a><a href="#">CONTACT</a>
    </nav>
    <div class="social" aria-label="Social links"><i></i><i></i><i></i></div>
  </footer>
</body>
</html>
```